Website Design for Korvelin.com.au (Design + Code)

I am a small business specialising in aquarium monitoring solutions.
Our products essentially are computerised monitoring equipment for aquariums. E.g. https://www.tidalmetrix.example/en-GB/products-shop/vantora-units
and also GloWard http://www.gloward.example/
I see the design having 3 pages
* Landing / Home
* Gallery
* Contact us
Design:
I am looking for a cutting edge slick looking site. It should have a number of pages so the site is interactive with contact us, gallery etc.
I have attached our logo and can provide more info as requested. I will be constantly changing the site content as well from my end.
I have attached my logo design which was done via MakerPlume. It can be changed/altered if you feel something else would work better
Final deliverable:
* This project requires both design and development (coding).
* The 3 design pages are to be delivered as PSD files, and the coding as HTML.
The site will need to scale to be viewable on both oSlate/otabs etc as well as standard desktop
Hi All,
Just based on the couple of designs that have come through so far I would like to specify that for the front landing page, I don't want to be product specific, but rather a page that describes the company and some information about what we do and why it is important to monitor your aquarium. It would still be good to have some images of the monitoring equipment, I will provide or modify the text with the information I am talking about above.
I hope this a little more specific.
Hi All,
While I like the designs that are coming through, I still feel that they are all very template based in look and feel.
I am looking for a unique design that is interactive and engaging to the viewer.
If you need more information from me, please let me know.
Please feel free to submit completely new designs.
Kind Regards,
Tarvesh

```html
<!DOCTYPE html>
<html lang="en">
<head>
<meta charset="utf-8">
<title>Korvelin – Aquarium Monitoring</title>
<link rel="stylesheet" href="https://fonts.googleapis.com/css2?family=Arimo:wght@400;700&display=swap">
<style>
:root{
  --canvas:#f6f6f6;
  --page:#ffffff;
  --blue:#4aa8df;
  --blue-dark:#1f8fcf;
  --blue-text:#2b9ad8;
  --nav-active:#585858;
  --ink:#222222;
  --ink-soft:#444444;
  --muted:#8a8a8a;
  --line:#dddddd;
  --panel:#555555;
  --products-bg:#eaf3f9;
  --field-bg:#f1f8fd;
  --footer-bg:#f3f3f3;
  --sea-deep:#0a3a6e;
  --sea-mid:#17609f;
  --sea-light:#2f86c2;
}
*{box-sizing:border-box;margin:0;padding:0}
html,body{width:1160px;height:1200px;overflow:hidden}
body{background:var(--canvas);font-family:"Arimo",Arial,sans-serif;color:var(--ink);position:relative}
.header{position:absolute;left:149px;top:0;width:848px;height:110px}
.brand{position:absolute;left:0;top:42px;display:flex;align-items:center;gap:10px}
.brand-mark{width:26px;height:26px;background:var(--blue)}
.brand-name{font-size:34px;font-weight:400;color:var(--ink-soft);letter-spacing:.5px}
.social{position:absolute;right:0;top:18px;display:flex;gap:8px}
.social-dot{width:28px;height:28px;border-radius:50%;border:2px solid #c8c8c8}
.phone{position:absolute;right:0;top:68px;display:flex;align-items:center;gap:8px;font-size:18px;font-weight:700;color:var(--ink-soft)}
.page{position:absolute;left:149px;top:110px;width:848px;height:1052px;background:var(--page);box-shadow:0 2px 6px rgba(0,0,0,.25)}
.nav{position:absolute;left:0;top:0;width:848px;height:40px;background:var(--blue);display:flex;font-size:15px;color:#fff}
.nav a{color:#fff;text-decoration:none;line-height:40px;position:absolute;top:0}
.nav .active{background:var(--nav-active);width:79px;text-align:center;left:0}
.hero{position:absolute;left:0;top:40px;width:848px;height:325px}
.hero-photo{position:absolute;inset:0;background:radial-gradient(ellipse at 35% 0%,var(--sea-light),var(--sea-mid) 45%,var(--sea-deep))}
.hero-title{position:absolute;left:23px;top:48px;font-size:43px;font-weight:700;color:#fff;letter-spacing:-.5px}
.hero-text{position:absolute;left:23px;top:100px;width:480px;font-size:14px;font-weight:700;line-height:21.6px;color:#fff}
.slider{position:absolute;right:21px;top:283px;display:flex;align-items:center;gap:7px}
.slider-dot{width:11px;height:11px;border-radius:50%;background:#fff}
.slider-arrow{width:20px;height:20px}
.welcome{position:absolute;left:22px;top:387px;width:539px;height:248px;border:1px solid var(--line);padding:20px 14px}
.welcome h1{font-size:18px;font-weight:400;color:var(--ink);margin-bottom:14px}
.welcome p{font-size:12px;line-height:17.4px;color:var(--ink-soft)}
.welcome p+p{margin-top:17px}
.read-more{display:block;margin-top:18px;font-size:12px;font-weight:700;color:var(--blue-text);text-decoration:none}
.products{position:absolute;left:22px;top:646px;width:539px;height:247px;border:1px solid var(--line);background:var(--products-bg)}
.panel-head{height:42px;background:var(--blue);color:#fff;font-size:17px;font-weight:700;line-height:42px;padding-left:14px}
.product{position:absolute;top:60px;width:120px;text-align:center}
.product-photo{height:78px;margin:0 12px;background:linear-gradient(#3a3a3a,#1e1e1e);border-radius:4px}
.product-name{margin-top:16px;font-size:12px;color:var(--ink-soft)}
.product-price{margin-top:3px;font-size:12px;font-weight:700;color:var(--blue-text)}
.btn{display:block;background:linear-gradient(var(--blue),var(--blue-dark));color:#fff;font-size:12px;font-weight:700;text-align:center;border:1px solid #1b7fb9}
.product .btn{width:96px;height:27px;line-height:25px;margin:5px auto 0}
.carousel-arrow{position:absolute;top:135px;width:20px;height:20px}
.contact{position:absolute;left:582px;top:388px;width:243px;height:352px;background:var(--panel)}
.contact .panel-head{font-weight:400;font-size:18px;display:flex;justify-content:space-between;align-items:center;padding-right:12px}
.contact form{padding:12px 14px}
.contact label{display:block;font-size:12px;color:#fff;margin-bottom:5px}
.field{width:215px;height:29px;background:#fff;border:none;margin-bottom:13px}
.field-area{height:62px;background:var(--field-bg);padding:6px 8px;font-size:11px;color:var(--ink-soft)}
.contact .btn{width:96px;height:28px;line-height:26px;margin:11px auto 0}
.footer{position:absolute;left:0;top:944px;width:848px;height:108px;background:var(--footer-bg);border-top:1px solid #e2e2e2}
.footer-brand{position:absolute;left:21px;top:34px;display:flex;align-items:center;gap:6px}
.footer-brand .brand-mark{width:14px;height:14px}
.footer-brand span{font-size:14px;color:var(--ink-soft)}
.footer-info{position:absolute;left:0;right:0;top:18px;text-align:center;font-size:11.5px;color:var(--muted);line-height:18px}
.footer-info b{color:var(--ink)}
.footer-info .sep{margin:0 8px;color:#bbb}
.footer-social{position:absolute;left:0;right:0;top:60px;display:flex;justify-content:center;gap:8px}
.footer-social .social-dot{width:29px;height:29px;border-color:#555}
.footer-social .social-dot.blue{border-color:var(--blue)}
</style>
</head>
<body>
<header class="header">
  <div class="brand"><span class="brand-mark"></span><span class="brand-name">Korvelin</span></div>
  <div class="social"><span class="social-dot"></span><span class="social-dot"></span><span class="social-dot"></span></div>
  <div class="phone">
    <svg width="24" height="24" viewBox="0 0 24 24"><circle cx="12" cy="12" r="11" fill="none" stroke="#2b9ad8" stroke-width="2"/><path d="M8 6.5c-1 1-1 3 1 6s4.5 5 6 4.8l1.3-1.5-2.2-1.8-1.3 1c-1.3-.6-3-2.5-3.5-3.7l1-1.2L8.8 6z" fill="#2b9ad8"/></svg>
    <span>0297 - 41 58 26</span>
  </div>
</header>

<main class="page">
  <nav class="nav">
    <a class="active" href="#">Home</a>
    <a href="#" style="left:97px">About us</a>
    <a href="#" style="left:162px">Products &amp; Service</a>
    <a href="#" style="left:350px">Gallery</a>
    <a href="#" style="left:415px">Solutions</a>
    <a href="#" style="left:512px">Contact</a>
  </nav>

  <section class="hero">
    <div class="hero-photo" role="img" aria-label="Underwater photograph of a sea turtle and fish swimming in deep blue ocean light"></div>
    <h2 class="hero-title">The Astounding Lives.</h2>
    <p class="hero-text">You can play a critical role in inspiring conservation of the oceans by joining one of our esteemed Donor Circles, including us in your estate plan or becoming a Business Partner.</p>
    <div class="slider">
      <span class="slider-dot"></span><span class="slider-dot"></span><span class="slider-dot"></span><span class="slider-dot"></span><span class="slider-dot"></span>
      <svg class="slider-arrow" viewBox="0 0 20 20"><circle cx="10" cy="10" r="9" fill="none" stroke="#fff" stroke-width="2"/><path d="M12 5.5 6.5 10 12 14.5z" fill="#fff"/></svg>
      <svg class="slider-arrow" viewBox="0 0 20 20"><circle cx="10" cy="10" r="9" fill="none" stroke="#fff" stroke-width="2"/><path d="M8 5.5 13.5 10 8 14.5z" fill="#fff"/></svg>
    </div>
  </section>

  <section class="welcome">
    <h1>Welcome to Korvelin Aquarium Monitoring</h1>
    <p>Mijn naam is Sanne Velthuis en ik ben 25 jaar oud. Vanaf februari 2012 ben ik begonnen aan de opleiding voor pedicure, deze opleiding volg ik bij<br>Veldhof-opleidingen in Rotterdam.</p>
    <p>het is nu mei en ik ben geslaagd voor mijn laatste theorie examen!! vanaf 20 mei kan ik opgeroepen worden voor het praktijk examen dus dat schiet ook al op.<br>ik heb het afgelopen jaar erg veel geleerd en er valt nog veel meer te leren in dit vak, wat ik ook zeker wil blijven doen.</p>
    <a class="read-more" href="#">Read more</a>
  </section>

  <section class="products">
    <div class="panel-head">Our products</div>
    <svg class="carousel-arrow" style="left:13px" viewBox="0 0 20 20"><circle cx="10" cy="10" r="9" fill="#fff" stroke="#aaa" stroke-width="1.5"/><path d="M12 6 7 10l5 4z" fill="#999"/></svg>
    <div class="product" style="left:62px">
      <div class="product-photo" role="img" aria-label="Product photo of a Vantora expansion box"></div>
      <div class="product-name">Vantora Controller</div>
      <div class="product-price">€34,59</div>
      <a class="btn" href="#">Buy</a>
    </div>
    <div class="product" style="left:231px">
      <div class="product-photo" role="img" aria-label="Product photo of a Vantora touch display unit"></div>
      <div class="product-name">Vantora Controller</div>
      <div class="product-price">€34,59</div>
      <a class="btn" href="#">Buy</a>
    </div>
    <div class="product" style="left:400px">
      <div class="product-photo" role="img" aria-label="Product photo of a Vantora controller unit"></div>
      <div class="product-name">Vantora Controller</div>
      <div class="product-price">€34,59</div>
      <a class="btn" href="#">Buy</a>
    </div>
    <svg class="carousel-arrow" style="left:504px" viewBox="0 0 20 20"><circle cx="10" cy="10" r="9" fill="#fff" stroke="#aaa" stroke-width="1.5"/><path d="M8 6l5 4-5 4z" fill="#999"/></svg>
  </section>

  <aside class="contact">
    <div class="panel-head">Quick Contact
      <svg width="28" height="22" viewBox="0 0 28 22"><path d="M2 8 14 1l12 7v13H2z" fill="#1e5a86"/><path d="M2 8l12 8 12-8v13H2z" fill="#fff"/><path d="M2 21l9-8M26 21l-9-8" stroke="#1e5a86" stroke-width="1.5"/></svg>
    </div>
    <form>
      <label>Name</label><div class="field"></div>
      <label>Phone no.</label><div class="field"></div>
      <label>Email</label><div class="field"></div>
      <label>Your enquire.</label><div class="field field-area">Enter your message here</div>
      <a class="btn" href="#">Send</a>
    </form>
  </aside>

  <footer class="footer">
    <div class="footer-brand"><span class="brand-mark"></span><span>Korvelin</span></div>
    <div class="footer-info">
      <b>Phone.</b> : 0297 - 41 58 26<span class="sep">|</span><b>Mob.</b>: 06 - 58 12 90 47<span class="sep">|</span><b>E-mail</b>: info@korvelin.com.au<br>
      © All Rights Reserved <b>Korvelin</b>
    </div>
    <div class="footer-social"><span class="social-dot"></span><span class="social-dot blue"></span><span class="social-dot"></span></div>
  </footer>
</main>
</body>
</html>
```